Coffee House With Cycling Theme Wants Business Cards

We want to create a business card for a coffee house that has a cycling theme. We expect to use the current logo on one side of the business card and we have been considering adding the words 'COFFEE HOUSE' underneath (see example). For the other side of the business card we want an interesting design with tag-line, address and social media links (the normal business card stuff). See examples provided but we are not fixed on having it exactly as shown, we are very open to great creative ideas. Please note our logo has the initials ‘RM' in orange embedded in the design and this must be retained. However, you can play with the words COFFEE HOUSE as well as use the orange color on the backside of the business card, as you see fit. For an image on the backside of the business card it can be a photo, hand-drawn or whatever but it must visually combine coffee and cycling in some way. The interior of the Coffee House will be reclaimed wood, rustic and have an urban feel to it with cycling artifacts hanging from the walls/ceiling, etc. Finally, it would be beneficial if the business card design elements can be easily used on flyers and other promotional assets. Good luck, we are looking forward to seeing your creative ideas.

Target Market(s)

Coffee lovers and cycling fans

Contact Information for Business Card

See project description.

Colors

Designer to choose colors to be used in the design.

Requirements
Must have
• Must use the current logo provided and combine a coffee and bike theme.
Nice to have
• Orange is used in current logo and could be used as an accent color on the backside of the business card.

```html
<!DOCTYPE html>
<html lang="en">
<head>
<meta charset="utf-8">
<title>RM Coffee House – Business Card Concepts</title>
<link href="https://fonts.googleapis.com/css2?family=Fira+Sans:wght@400;500;700&display=swap" rel="stylesheet">
<style>
  :root {
    --orange: #f0682a;
    --charcoal: #404040;
    --ink: #333333;
    --paper: #ffffff;
    --backdrop: #e9e6e2;
    --strip-dark: #444444;
    --strip-mid: #7a7a7a;
  }
  * { box-sizing: border-box; margin: 0; padding: 0; }
  html, body {
    width: 1154px; height: 1200px; overflow: hidden;
    background: var(--backdrop);
    font-family: "Fira Sans", sans-serif;
    color: var(--ink);
  }
  .canvas { position: relative; width: 1154px; height: 1200px; }

  /* Logo variations sheet */
  .logo-sheet {
    position: absolute; left: 28px; top: 10px; width: 736px; height: 552px;
    background: var(--paper);
    display: grid; grid-template-columns: repeat(3, 1fr); grid-template-rows: repeat(3, 1fr);
    padding: 10px 12px;
  }
  .logo-variant {
    display: flex; flex-direction: column; align-items: center; justify-content: center;
    font-weight: 700; line-height: 0.95; text-transform: uppercase;
  }
  .logo-variant .mark { font-size: 78px; letter-spacing: 2px; }
  .logo-variant .words { font-size: 26px; letter-spacing: 1px; }
  .logo-variant .variant-no { font-size: 12px; color: var(--ink); margin-top: 8px; font-weight: 500; }
  .tone-dark { color: var(--charcoal); }
  .tone-orange { color: var(--orange); }

  /* Business card backs */
  .card {
    position: absolute; width: 315px; height: 552px;
    background: var(--paper);
  }
  .card-1 { left: 811px; top: 12px; }
  .card-2 { left: 28px; top: 602px; }
  .card-3 { left: 424px; top: 602px; }
  .card-4 { left: 812px; top: 600px; }

  .card .tagline {
    position: absolute; left: 26px; top: var(--tag-top);
    font-size: 17.6px; font-weight: 500; line-height: 21px; color: var(--ink);
    white-space: nowrap; letter-spacing: 0.2px;
  }
  .card .address {
    position: absolute; left: 26px; top: var(--addr-top);
    font-size: 12.8px; font-weight: 500; line-height: 16px; white-space: nowrap;
  }
  .accent { color: var(--orange); }
  .dot-sep { color: var(--orange); margin: 0 5px; font-size: 9px; vertical-align: 2px; }

  .card .artwork {
    position: absolute; left: var(--art-left); top: var(--art-top);
    width: var(--art-w); height: var(--art-h);
    border-radius: 50%;
  }
  .card-1 { --tag-top: 97px; --addr-top: 153px; --art-left: 34px; --art-top: 218px; --art-w: 138px; --art-h: 118px; --contact-top: 398px; }
  .card-2 { --tag-top: 96px; --addr-top: 151px; --art-left: 56px; --art-top: 205px; --art-w: 118px; --art-h: 136px; --contact-top: 410px; }
  .card-3 { --tag-top: 97px; --addr-top: 152px; --art-left: 54px; --art-top: 244px; --art-w: 134px; --art-h: 84px; --contact-top: 412px; }
  .card-4 { --tag-top: 84px; --addr-top: 138px; --art-left: 48px; --art-top: 204px; --art-w: 168px; --art-h: 148px; --contact-top: 404px; }

  .card-1 .artwork { background: radial-gradient(ellipse at center, #4a4a4a 0%, #8a8480 40%, #f1c2a8 62%, var(--paper) 74%); }
  .card-2 .artwork { background: radial-gradient(ellipse at center, #6a6a6a 0%, #b8b2ad 42%, #f6cdb5 62%, var(--paper) 74%); }
  .card-3 .artwork { background: radial-gradient(ellipse at center, #b79a80 0%, #e6e2de 50%, var(--paper) 74%); }
  .card-4 .artwork { background: radial-gradient(ellipse at center, #8a5a35 0%, #d9c7b6 45%, var(--paper) 74%); }

  .card .contact {
    position: absolute; left: 26px; top: var(--contact-top);
    font-size: 13px; font-weight: 500; line-height: 20px; white-space: nowrap;
  }
  .social { display: flex; align-items: center; gap: 6px; margin-top: 3px; }
  .social .badge { width: 14px; height: 14px; border-radius: 50%; background: var(--orange); flex: none; }

  .card .cycle-strip {
    position: absolute; right: 6px; top: 6px; width: 50px; height: 540px;
    border-radius: 25px;
    background:
      linear-gradient(90deg, var(--strip-mid) 0%, var(--strip-dark) 30%, #9a9a9a 50%, var(--strip-dark) 70%, var(--strip-mid) 100%);
    opacity: 0.85;
  }

  .card-label {
    position: absolute; font-size: 20px; font-weight: 500; color: var(--ink);
    transform: translateX(-50%);
  }
</style>
</head>
<body>
<div class="canvas">

  <section class="logo-sheet" aria-label="Logo colour variations">
    <div class="logo-variant tone-dark"><span class="mark">RM</span><span class="words">Coffee House</span><span class="variant-no">1</span></div>
    <div class="logo-variant tone-orange"><span class="mark">RM</span><span class="words">Coffee House</span><span class="variant-no">2</span></div>
    <div class="logo-variant tone-orange"><span class="mark">RM</span><span class="words">Coffee House</span><span class="variant-no">3</span></div>
    <div class="logo-variant tone-orange"><span class="mark">RM</span><span class="words">Coffee House</span><span class="variant-no">4</span></div>
    <div class="logo-variant tone-dark"><span class="mark">RM</span><span class="words">Coffee House</span><span class="variant-no">5</span></div>
    <div class="logo-variant tone-dark"><span class="mark">RM</span><span class="words">Coffee House</span><span class="variant-no">6</span></div>
    <div class="logo-variant tone-orange"><span class="mark">RM</span><span class="words">Coffee House</span><span class="variant-no">7</span></div>
    <div class="logo-variant tone-orange"><span class="mark">RM</span><span class="words">Coffee House</span><span class="variant-no">8</span></div>
    <div class="logo-variant tone-dark"><span class="mark">RM</span><span class="words">Coffee House</span><span class="variant-no">9</span></div>
  </section>

  <article class="card card-1">
    <p class="tagline">great coffee with a<br>cycling flavored ambiance<span class="accent">.</span></p>
    <p class="address">123 Coffee House Street<span class="dot-sep">●</span>City Ville</p>
    <div class="artwork" role="img" aria-label="Illustration of a steaming coffee cup on a saucer with orange steam"></div>
    <div class="contact">
      <p>www<span class="accent">.</span>rmcoffeehouse<span class="accent">.</span>com</p>
      <p>casey<span class="accent">@</span>rmcoffeehouse<span class="accent">.</span>com</p>
      <p class="social"><span class="badge"></span>@rmcoffeehouse</p>
    </div>
    <div class="cycle-strip" role="img" aria-label="Vertical border of repeating bicycles alternating with coffee cups"></div>
  </article>
  <span class="card-label" style="left:974px; top:572px;">1</span>

  <article class="card card-2">
    <p class="tagline">Great Coffee with a<br>Cycling Flavored Ambiance<span class="accent">.</span></p>
    <p class="address">123 Coffee House Street<span class="dot-sep">●</span>City Ville</p>
    <div class="artwork" role="img" aria-label="Line illustration of a coffee cup with orange steam"></div>
    <div class="contact">
      <p>www<span class="accent">.</span>rmcoffeehouse<span class="accent">.</span>com</p>
      <p>casey<span class="accent">@</span>rmcoffeehouse<span class="accent">.</span>com</p>
      <p class="social"><span class="badge"></span>@rmcoffeehouse</p>
    </div>
    <div class="cycle-strip" role="img" aria-label="Vertical border of repeating bicycles alternating with coffee cups"></div>
  </article>
  <span class="card-label" style="left:187px; top:1162px;">2</span>

  <article class="card card-3">
    <p class="tagline">Great Coffee with a<br>Cycling Flavored Ambiance<span class="accent">.</span></p>
    <p class="address">123 Coffee House Street<span class="dot-sep">●</span>City Ville</p>
    <div class="artwork" role="img" aria-label="Photo of a latte in a white cup on a saucer"></div>
    <div class="contact">
      <p>www<span class="accent">.</span>rmcoffeehouse<span class="accent">.</span>com</p>
      <p>casey<span class="accent">@</span>rmcoffeehouse<span class="accent">.</span>com</p>
      <p class="social"><span class="badge"></span>@rmcoffeehouse</p>
    </div>
    <div class="cycle-strip" role="img" aria-label="Vertical border of repeating bicycles alternating with coffee cups"></div>
  </article>
  <span class="card-label" style="left:573px; top:1164px;">3</span>

  <article class="card card-4">
    <p class="tagline">Great Coffee with a<br>Cycling Flavored Ambiance<span class="accent">.</span></p>
    <p class="address">123 Coffee House Street<span class="dot-sep">●</span>City Ville</p>
    <div class="artwork" role="img" aria-label="Photo of espresso, latte art and coffee beans in small cups arranged like a bicycle"></div>
    <div class="contact">
      <p>www<span class="accent">.</span>rmcoffeehouse<span class="accent">.</span>com</p>
      <p>casey<span class="accent">@</span>rmcoffeehouse<span class="accent">.</span>com</p>
      <p class="social"><span class="badge"></span>@rmcoffeehouse</p>
    </div>
    <div class="cycle-strip" role="img" aria-label="Vertical border of repeating bicycles alternating with coffee cups"></div>
  </article>
  <span class="card-label" style="left:968px; top:1168px;">4</span>

</div>
</body>
</html>
```